Visitenkartenerstellung für Dorvek-Estates
Zielgruppe
Männer und Frauen, junge Familien bis hin zum Senior.
Verkauf von hochwertigen Immobilien in Spanien.
Aufgabenstellung
Auf Grund unserer Namensänderung benötigen wir ein neues Visitenkartendesign.
Wir sind eine skandinavische Agentur für Luxus-Immobilien auf Mallorca.
Das Design sollte dementsprechend edel aber dennoch schlicht gestaltet sein!

```html
<!DOCTYPE html>
<html lang="de">
<head>
<meta charset="utf-8">
<title>Dorvek-Estates – Visitenkarte</title>
<link rel="stylesheet" href="https://fonts.googleapis.com/css2?family=Lato:wght@300;400;900&display=swap">
<style>
  :root {
    --page: #ffffff;
    --card: #ffffff;
    --brand-blue: #1f4d7c;
    --text-blue: #4f7eab;
    --card-edge: rgba(0, 0, 0, 0.06);
    --card-shadow: rgba(0, 0, 0, 0.16);
  }
  html, body {
    margin: 0;
    padding: 0;
    overflow: hidden;
    background: var(--page);
  }
  .canvas {
    position: relative;
    width: 1200px;
    height: 687px;
    background: var(--page);
    overflow: hidden;
    font-family: "Lato", sans-serif;
  }
  .card {
    position: absolute;
    top: 173px;
    width: 529px;
    height: 340px;
    background: var(--card);
    border: 1px solid var(--card-edge);
    box-shadow: 3px 4px 8px var(--card-shadow);
    box-sizing: border-box;
  }
  .card--front { left: 53px; }
  .card--back { left: 618px; }

  .brand {
    position: absolute;
    left: 0;
    right: 0;
    top: 104px;
    text-align: center;
  }
  .brand__name {
    margin: 0;
    font-weight: 300;
    font-size: 66px;
    line-height: 1;
    letter-spacing: 0.5px;
    color: var(--brand-blue);
  }
  .brand__tagline {
    margin: 40px 0 0;
    font-weight: 300;
    font-size: 17px;
    letter-spacing: 1.2px;
    color: var(--text-blue);
    text-transform: uppercase;
  }

  .contact {
    position: absolute;
    left: 27px;
    top: 126px;
    color: var(--text-blue);
    text-transform: uppercase;
  }
  .contact__headline {
    margin: 0 0 18px;
    font-size: 21px;
    font-weight: 300;
    line-height: 24px;
  }
  .contact__name {
    font-weight: 900;
    color: var(--brand-blue);
    letter-spacing: 0.6px;
  }
  .contact__role {
    letter-spacing: 0.3px;
  }
  .contact__block {
    margin: 0 0 21px;
    font-style: normal;
    font-weight: 300;
    font-size: 17px;
    line-height: 21px;
    letter-spacing: 0.2px;
  }
  .contact__block p { margin: 0; }
</style>
</head>
<body>
  <main class="canvas">
    <section class="card card--front" aria-label="Vorderseite">
      <div class="brand">
        <h1 class="brand__name">Dorvek-Estates</h1>
        <p class="brand__tagline">Luxury real estate on Mallorca and Ibiza</p>
      </div>
    </section>

    <section class="card card--back" aria-label="Rückseite">
      <div class="contact">
        <h2 class="contact__headline">
          <span class="contact__name">Linnea Halvorsen</span>
          <span class="contact__role">Property Manager</span>
        </h2>
        <address class="contact__block">
          <p>C. Almendro 12</p>
          <p>07190 Sant Olmo Spain</p>
        </address>
        <div class="contact__block">
          <p>Tel. 971555218</p>
          <p>Mobil 0034 61255847</p>
          <p>linnea.halvorsen@dorvek-estates.com</p>
          <p>www.dorvek-estates.se</p>
        </div>
      </div>
    </section>
  </main>
</body>
</html>
```